Sparkbench Co: Fun, Clean Website Banner Design!

Sparkbench Co is passionate about bringing the world of science to all young Australians, and making it FUN!

We need a new website banner designed for our website www.wildovergadgets.com.au

We need two versions of the same banner - one with some Christmas embellishments and one without.

The banner should be eye-catching, clean and professional looking. It should fit in with our website page design. See our existing sliding banner designs to get an idea of the look and feel at www.wildovergadgets.com.au

It should include some text, a background image for context (perhaps a desk?) or graphic element, a call to action button, as well as some images of desktop toys we sell, see attached. Not all have to be included. The call to action button is BROWSE ALL ITEMS.

The banner measures 1102 x 415 px

Banner Text:
Desktop Science
Curiosities for your desk or classroom

Target Market(s)

Parents of curious kids, science enthusiasts and teachers

Contact Information for Business Card

Include logo (attached image), some samples of singage we've had designed are attached for inspiration. Would be open to single or double sided design.
Feel is modern sophisticated, modern, progressive, eye-cathcing. Balance between seious and fun to appeal to all segments of our market - serious schools as well as fun for kids.
May not include dots, as trying to mature from too young and silly.
Text detail to include:
Name
Position
Seriously Fun!
www.wildovergadgets.com.au
name@wildovergadgets.com.au
2B/476 Harlow Rd, Kelverton, VIC, 3928
1300 417 286
Fax: 03 7514 3982

Science Shop
School Workshops
Parties & Events
Lab Supplies & Teacher Resources

Font styles to use
Sans Serif

Requirements
Must have
• We need two versions of the same banner - one with Christmas embellishments and one without.
• Images of desktop toys we sell, see attached. Not all have to be included.
• Call to action button BROWSE ALL ITEMS.
• Banner Text:
• Desktop Science
• Curiosities for your desk or classroom
Nice to have
• A background image for context such as a desk? or a graphic element
Should not have
• Fun and exciting, but not too young and immature.

```html
<!DOCTYPE html>
<html lang="en">
<head>
<meta charset="utf-8">
<title>Sparkbench Co – Desktop Science</title>
<link rel="stylesheet" href="https://fonts.googleapis.com/css2?family=Montserrat:wght@600;700&family=Nunito+Sans:wght@500;600&display=swap">
<style>
  :root {
    --bg-coral: #f8827c;
    --pattern-coral: #f26c66;
    --ink: #2a2628;
    --desk-top: #f1e7e2;
    --desk-edge: #ddd1cb;
    --desk-shadow: #c9bcb6;
    --leg: #1d1b1c;
    --cta: #4b9b46;
    --cta-text: #ffffff;
    --frame: #111111;
    --frame-inner: #f4f4f4;
    --frame-shade: #d9d9d9;
    --brand-ink: #2d4fa8;
  }
  * { margin: 0; padding: 0; box-sizing: border-box; }
  html, body { width: 1200px; height: 452px; overflow: hidden; background: var(--bg-coral); }
  .banner {
    position: relative;
    width: 1200px;
    height: 452px;
    overflow: hidden;
    background: var(--bg-coral);
    font-family: "Nunito Sans", Arial, sans-serif;
  }
  .festive-pattern {
    position: absolute;
    inset: 0;
    background: radial-gradient(ellipse at 40% 40%, var(--bg-coral) 0%, var(--bg-coral) 55%, var(--pattern-coral) 130%);
  }
  .brand-frame {
    position: absolute;
    left: 998px;
    top: -6px;
    width: 214px;
    height: 124px;
    background: var(--frame);
    padding: 9px;
  }
  .brand-frame__mat {
    width: 100%;
    height: 100%;
    background: linear-gradient(155deg, var(--frame-inner) 0%, var(--frame-inner) 55%, var(--frame-shade) 56%, var(--frame-inner) 100%);
    display: flex;
    justify-content: center;
    padding-top: 16px;
    padding-right: 12px;
  }
  .brand-name {
    font-family: "Montserrat", Arial, sans-serif;
    font-weight: 700;
    font-size: 18px;
    color: var(--brand-ink);
    white-space: nowrap;
  }
  .headline {
    position: absolute;
    left: 40px;
    top: 77px;
    width: 510px;
    text-align: center;
    color: var(--ink);
  }
  .headline__title {
    font-family: "Montserrat", Arial, sans-serif;
    font-weight: 700;
    font-size: 45px;
    letter-spacing: 2.5px;
    line-height: 52px;
    white-space: nowrap;
  }
  .headline__sub {
    margin-top: 16px;
    font-size: 41px;
    font-weight: 500;
    line-height: 54px;
    letter-spacing: 1.3px;
    white-space: nowrap;
  }
  .cta {
    position: absolute;
    left: 172px;
    top: 282px;
    width: 245px;
    height: 53px;
    background: var(--cta);
    color: var(--cta-text);
    font-size: 18px;
    font-weight: 600;
    display: flex;
    align-items: center;
    justify-content: center;
    text-decoration: none;
    letter-spacing: 0.3px;
  }
  .desk {
    position: absolute;
    left: 0;
    top: 313px;
    width: 1200px;
    height: 139px;
  }
  .product { position: absolute; }
  .product--pendulum { left: 545px; top: 114px; width: 192px; height: 245px; }
  .product--engine { left: 751px; top: 142px; width: 183px; height: 234px; }
  .product--sand { left: 975px; top: 169px; width: 192px; height: 182px; }
</style>
</head>
<body>
<main class="banner">
  <div class="festive-pattern" role="img" aria-label="Coral background with a soft pattern of snowflakes, stockings and stars"></div>

  <div class="brand-frame">
    <div class="brand-frame__mat">
      <span class="brand-name">Sparkbench Co</span>
    </div>
  </div>

  <svg class="desk" viewBox="0 0 1200 139" aria-hidden="true">
    <rect x="28" y="100" width="30" height="39" fill="var(--leg)"/>
    <rect x="1150" y="100" width="30" height="39" fill="var(--leg)"/>
    <rect x="0" y="0" width="1200" height="92" fill="var(--desk-top)"/>
    <rect x="0" y="92" width="1200" height="14" fill="var(--desk-edge)"/>
    <rect x="0" y="106" width="1200" height="4" fill="var(--desk-shadow)"/>
  </svg>

  <section class="headline">
    <h1 class="headline__title">DESKTOP SCIENCE</h1>
    <p class="headline__sub">Curiosities for your<br>desk or classroom</p>
  </section>

  <a class="cta" href="#">Browse All Items</a>

  <svg class="product product--pendulum" viewBox="0 0 192 245" role="img" aria-label="Photo of a kinetic pendulum desk toy with coloured metallic balls on a black stand">
    <defs>
      <linearGradient id="pendulumTone" x1="0" y1="0" x2="0" y2="1">
        <stop offset="0" stop-color="#8a6f9a"/>
        <stop offset="0.55" stop-color="#4b4a52"/>
        <stop offset="1" stop-color="#1c1c1e"/>
      </linearGradient>
    </defs>
    <rect x="4" y="4" width="184" height="237" rx="20" fill="url(#pendulumTone)" opacity="0.9"/>
  </svg>

  <svg class="product product--engine" viewBox="0 0 183 234" role="img" aria-label="Photo of a brass and chrome Stirling engine model with a large flywheel">
    <defs>
      <linearGradient id="engineTone" x1="0" y1="0" x2="0" y2="1">
        <stop offset="0" stop-color="#d8a43a"/>
        <stop offset="0.6" stop-color="#c9c1b4"/>
        <stop offset="1" stop-color="#5a5f63"/>
      </linearGradient>
    </defs>
    <rect x="4" y="4" width="175" height="226" rx="20" fill="url(#engineTone)" opacity="0.9"/>
  </svg>

  <svg class="product product--sand" viewBox="0 0 192 182" role="img" aria-label="Photo of a round moving sand art frame with blue sand on a dark stand">
    <defs>
      <linearGradient id="sandTone" x1="0" y1="0" x2="0" y2="1">
        <stop offset="0" stop-color="#bfe3f3"/>
        <stop offset="0.6" stop-color="#3f8fc4"/>
        <stop offset="1" stop-color="#2b2b2e"/>
      </linearGradient>
    </defs>
    <rect x="4" y="4" width="184" height="174" rx="22" fill="url(#sandTone)" opacity="0.9"/>
  </svg>
</main>
</body>
</html>
```